A new presentation to our clients

we are a Real Estate agency, our website is www.lirotama.com and it’s time to have a new, fashion and remarcable Business Card. we want to differentiate ourselves from other companies so we want a business card that differentiates us. we want the business card to impact our customers. in the competitive market that we have today, we have to be different and it is this difference that we seek

Target Market(s)

Real Estate Clients

Contact Information for Business Card

We search a totaly diferent card from the usual

Font styles to use
Sans Serif

Colors
e34197

Requirements
Must have
• Logo, adress, phone contact, e-mail, photo, and our website
Nice to have
• We would like to see a modern business card
Should not have
• Houses or building draws

```html
<!DOCTYPE html>
<html lang="pt">
<head>
<meta charset="utf-8">
<title>Lirotama — Business Card</title>
<link rel="stylesheet" href="https://fonts.googleapis.com/css2?family=Montserrat:wght@400;500;600;700&display=swap">
<style>
  :root {
    --brand-pink: #e34197;
    --card-dark: #2d2d2e;
    --card-dark-mark: #3a2e34;
    --card-light: #f3f3f2;
    --ink: #3a3a3a;
    --backdrop: #9a9a9a;
    --on-dark: #f2f2f2;
  }
  * { box-sizing: border-box; margin: 0; padding: 0; }
  html, body { width: 1200px; height: 1200px; overflow: hidden; }
  body {
    background: var(--backdrop);
    font-family: "Montserrat", sans-serif;
    position: relative;
  }
  .card {
    position: absolute;
    left: 200px;
    width: 800px;
    height: 457px;
    border-radius: 4px;
    overflow: hidden;
    box-shadow: 0 10px 28px rgba(0,0,0,0.25);
  }
  /* Back side */
  .card-back { top: 108px; background: var(--card-dark); }
  .card-back .mark-faint {
    position: absolute;
    left: 40px; top: 110px;
    font-size: 132px;
    font-weight: 700;
    letter-spacing: 2px;
    color: var(--card-dark-mark);
    white-space: nowrap;
  }
  .card-back .name-corner {
    position: absolute;
    right: 60px; bottom: 50px;
    font-size: 58px;
    font-weight: 700;
    color: var(--on-dark);
  }
  /* Front side */
  .card-front { top: 635px; background: var(--card-light); }
  .front-name {
    position: absolute;
    left: 58px; top: 120px;
    font-size: 64px;
    font-weight: 700;
    color: var(--brand-pink);
  }
  .details {
    position: absolute;
    left: 470px; top: 112px;
    width: 290px;
    color: var(--ink);
  }
  .person-name { font-size: 27px; font-weight: 700; color: var(--brand-pink); line-height: 1.1; }
  .person-role { font-size: 19px; font-weight: 600; margin-top: 2px; }
  .rule { height: 2px; background: var(--brand-pink); margin: 14px 0 12px; }
  .address { font-size: 17px; line-height: 1.3; font-style: normal; }
  .contacts { list-style: none; margin-top: 8px; }
  .contacts li {
    display: flex; align-items: center; gap: 10px;
    font-size: 18px; line-height: 1.55;
  }
  .contacts svg { width: 16px; height: 16px; fill: var(--brand-pink); flex: none; }
  .band {
    position: absolute;
    left: 0; right: 0; bottom: 28px;
    height: 13px;
    background: var(--brand-pink);
  }
</style>
</head>
<body>

<section class="card card-back" aria-label="Card back">
  <div class="mark-faint" aria-hidden="true">Lirotama</div>
  <div class="name-corner">Lirotama</div>
</section>

<section class="card card-front" aria-label="Card front">
  <div class="front-name">Lirotama</div>
  <div class="details">
    <div class="person-name">Mirela Vostan</div>
    <div class="person-role">Managing Director</div>
    <div class="rule"></div>
    <address class="address">Rua das Flores Altas, 118<br>4410-052, Porto Verde</address>
    <div class="rule"></div>
    <ul class="contacts">
      <li>
        <svg viewBox="0 0 16 16" aria-hidden="true"><path d="M3.6 1.2l2.3 2.6-1.3 2a9 9 0 0 0 5.6 5.6l2-1.3 2.6 2.3-1.2 2.4C7.6 14.6 1.4 8.4 1.2 2.4z"/></svg>
        (+351) 220 481 306
      </li>
      <li>
        <svg viewBox="0 0 16 16" aria-hidden="true"><path d="M4 1h8v4H4zM1 6h14v6h-3v3H4v-3H1zm4 4v4h6v-4z"/></svg>
        (+351) 220 481 309
      </li>
      <li>
        <svg viewBox="0 0 16 16" aria-hidden="true"><path d="M1 3h14v10H1zm1.5 1.3v.4L8 8.8l5.5-4.1v-.4z"/></svg>
        geral@lirotama.com
      </li>
      <li>
        <svg viewBox="0 0 16 16" aria-hidden="true"><circle cx="8" cy="8" r="7"/></svg>
        www.lirotama.com
      </li>
    </ul>
  </div>
  <div class="band"></div>
</section>

</body>
</html>
```